Brindle painting & waterproofing business card.

Business cards updated to reflect photos attached. we have given the photos of the old business cards and some of our updated designs for other items we have here in the office. Please see attached. if anyone needs to contact us directly for clarification you can email us at brindlerestoration@mailvane.com

Industry/Entity Type

Construction

Contact Information for Business Card

See attached photos

Font styles to use
Other font styles liked:
• Same as photos

Colors
ec1f27

Requirements
Must have
• Employee Names,
• Gordon Brindle II, Supervisor/Owner
• Gord Brindle, President/Owner
• Tim Harker, Sales Representative
• Lou Marsten, Supervisor
• Change 20 years to 25
Nice to have
• ideas reflecting the attached photos
Should not have
• should not be exactly like attached photos as those are old business card but reflect to match new logo listed as kelvar van and cup photo.

```html
<!DOCTYPE html>
<html lang="en">
<head>
<meta charset="utf-8">
<title>Brindle's Painting &amp; Restoration — Business Card</title>
<link rel="stylesheet" href="https://fonts.googleapis.com/css2?family=Montserrat:wght@500;600;700;800&display=swap">
<style>
  :root{
    --bg:#2b2d31;
    --card-white:#ffffff;
    --brand-orange:#ec4a22;
    --brand-red:#ec1f27;
    --ink:#2e2e30;
    --ink-soft:#55565a;
    --swoosh-light:#eeeff1;
    --swoosh-mid:#dcdde0;
  }
  *{box-sizing:border-box;margin:0;padding:0}
  html,body{width:1200px;height:900px;overflow:hidden;background:var(--bg);
    font-family:"Montserrat",Arial,sans-serif}
  .canvas{width:1200px;height:900px;display:flex;flex-direction:column;
    align-items:center;justify-content:center;gap:40px}
  .card{position:relative;width:700px;height:400px;overflow:hidden;
    box-shadow:0 10px 30px rgba(0,0,0,.35)}

  /* front */
  .card-front{background:var(--card-white);color:var(--ink)}
  .card-front .texture{position:absolute;inset:0}
  .wordmark{position:absolute;left:48px;top:40px;font-weight:800;
    color:var(--ink);line-height:1;text-transform:uppercase}
  .wordmark .w1{display:block;font-size:46px;letter-spacing:1px;color:var(--brand-red)}
  .wordmark .w2{display:block;font-size:28px;letter-spacing:3px;margin-top:6px;color:var(--brand-red)}
  .wordmark .w3{display:block;font-size:24px;letter-spacing:2px;margin-top:6px;color:var(--brand-red)}
  .rule-vertical{position:absolute;left:400px;top:150px;width:1.5px;height:110px;background:var(--brand-red)}
  .rule-horizontal{position:absolute;left:60px;right:0;top:300px;height:1.5px;background:var(--brand-red)}
  .contact{position:absolute;left:425px;top:140px}
  .contact .name{font-size:22px;font-weight:600;color:var(--brand-red);letter-spacing:.5px}
  .contact .role{font-size:14px;font-weight:600;color:var(--ink-soft);margin:2px 0 10px}
  .contact ul{list-style:none}
  .contact li{display:flex;align-items:center;gap:8px;font-size:13.5px;font-weight:600;
    color:var(--ink);margin-bottom:4px}
  .contact li svg{flex:none}
  .address{position:absolute;left:48px;top:318px;font-size:14px;font-weight:600;color:var(--ink)}
  .license{position:absolute;right:36px;bottom:24px;font-size:18px;font-weight:700;color:var(--brand-red)}

  /* back */
  .card-back{background:var(--brand-orange)}
  .card-back .wordmark{left:0;right:0;top:104px;text-align:center;color:#fff}
  .card-back .wordmark .w1{font-size:64px;color:#fff}
  .card-back .wordmark .w2{font-size:38px;color:#fff;margin-top:10px}
  .card-back .wordmark .w3{font-size:32px;color:#fff;margin-top:10px}
  .card-back .rule{position:absolute;left:60px;right:60px;top:88px;height:1px;background:rgba(255,255,255,.55)}
</style>
</head>
<body>
<main class="canvas">

  <section class="card card-front">
    <svg class="texture" width="700" height="400" viewBox="0 0 700 400" role="img" aria-label="Soft grey swoosh bands with a halftone dot texture">
      <defs>
        <linearGradient id="swooshFade" x1="0" y1="0" x2="1" y2="1">
          <stop offset="0" stop-color="#e6e7ea"/>
          <stop offset="1" stop-color="#f6f6f7"/>
        </linearGradient>
        <linearGradient id="redFade" x1="0" y1="0" x2="1" y2="0">
          <stop offset="0" stop-color="#ec1f27" stop-opacity="0"/>
          <stop offset="1" stop-color="#ec1f27" stop-opacity=".18"/>
        </linearGradient>
      </defs>
      <path d="M0 150 C200 120 450 170 700 120 L700 400 L0 400 Z" fill="url(#swooshFade)"/>
      <path d="M0 200 C250 170 480 250 700 210 L700 240 C480 280 250 205 0 230 Z" fill="#ffffff" opacity=".8"/>
      <path d="M160 400 C300 330 520 340 700 300 L700 330 C520 370 320 360 230 400 Z" fill="url(#redFade)"/>
    </svg>

    <div class="wordmark" aria-label="Brindle's Painting and Restoration">
      <span class="w1">Brindle's</span>
      <span class="w2">Painting &amp;</span>
      <span class="w3">Restoration</span>
    </div>

    <div class="rule-vertical"></div>

    <div class="contact">
      <p class="name">GORDON BRINDLE II</p>
      <p class="role">Owner/Supervisor</p>
      <ul>
        <li>
          <svg width="16" height="16" viewBox="0 0 16 16"><circle cx="8" cy="8" r="7" fill="none" stroke="var(--brand-red)" stroke-width="1.5"/><path d="M5.5 4.5 l1.5 0 l.6 1.8 -.9.8 a5 5 0 0 0 2.2 2.2 l.8-.9 1.8.6 0 1.5 a1 1 0 0 1-1 1 A6 6 0 0 1 4.5 5.5 a1 1 0 0 1 1-1z" fill="var(--brand-red)"/></svg>
          (954) 555-0142
        </li>
        <li>
          <svg width="16" height="16" viewBox="0 0 16 16"><circle cx="8" cy="8" r="7" fill="none" stroke="var(--brand-red)" stroke-width="1.5"/><rect x="4.5" y="5.5" width="7" height="5" fill="var(--brand-red)"/><path d="M4.5 5.5 L8 8.3 L11.5 5.5" fill="none" stroke="#fff" stroke-width=".9"/></svg>
          brindlerestoration@mailvane.com
        </li>
        <li>
          <svg width="16" height="16" viewBox="0 0 16 16"><circle cx="8" cy="8" r="7" fill="none" stroke="var(--brand-red)" stroke-width="1.5"/><circle cx="8" cy="8" r="4" fill="none" stroke="var(--brand-red)" stroke-width="1"/><path d="M4 8h8M8 4c-2 2.5-2 5.5 0 8M8 4c2 2.5 2 5.5 0 8" fill="none" stroke="var(--brand-red)" stroke-width=".8"/></svg>
          www.brindlerestoration.com
        </li>
      </ul>
    </div>

    <div class="rule-horizontal"></div>
    <p class="address">2400 NE 14th Ave . Coral Harbor, Florida 33060</p>
    <p class="license">CGC1840265</p>
  </section>

  <section class="card card-back">
    <div class="rule"></div>
    <div class="wordmark" aria-label="Brindle's Painting and Restoration">
      <span class="w1">Brindle's</span>
      <span class="w2">Painting &amp;</span>
      <span class="w3">Restoration</span>
    </div>
  </section>

</main>
</body>
</html>
```